Mabel's Fitness Business Cards

I would like my business cards to look expensive and sophisticated using my logo and the information below.

FRONT
Mabel’s Fitness logo

Tag line Become your happiest, healthiest and strongest self

Mabel Quint Harlow
Personal Trainer

e. mabel@mabelsfitstudio.example

t. 0781530462

w. www.mabelsfitstudio.example

```html
<!DOCTYPE html>
<html lang="en">
<head>
<meta charset="utf-8">
<title>Mabel's Fitness Business Cards</title>
<link href="https://fonts.googleapis.com/css2?family=Questrial&display=swap" rel="stylesheet">
<style>
  :root {
    --backdrop: #d8d6d6;
    --card: #000000;
    --teal: #6fb4be;
    --taupe: #a9a19f;
    --shadow: rgba(0, 0, 0, 0.28);
  }
  html, body {
    margin: 0;
    width: 1200px;
    height: 1200px;
    overflow: hidden;
    background: var(--backdrop);
    font-family: "Questrial", "Century Gothic", sans-serif;
  }
  .canvas { position: relative; width: 1200px; height: 1200px; }
  .card {
    position: absolute;
    left: 180px;
    width: 840px;
    height: 478px;
    background: var(--card);
    box-shadow: 5px 5px 5px var(--shadow);
  }
  .card--front { top: 98px; }
  .card--back { top: 622px; }

  .brand {
    position: absolute;
    width: 200px;
    margin-left: -100px;
    text-align: center;
  }
  .brand__ring {
    display: block;
    margin: 0 auto;
    width: 72px;
    height: 72px;
    border: 3px solid var(--teal);
    border-radius: 50%;
    box-sizing: border-box;
  }
  .brand__name {
    display: block;
    margin-top: 12px;
    color: var(--teal);
    font-size: 15px;
    letter-spacing: 4px;
    text-transform: uppercase;
    white-space: nowrap;
  }
  .card--front .brand { left: 218px; top: 172px; }
  .card--back .brand { left: 424px; top: 172px; }

  .identity {
    position: absolute;
    left: 412px;
    top: 104px;
    width: 320px;
    text-align: center;
  }
  .identity__name {
    margin: 0;
    color: var(--teal);
    font-size: 33px;
    font-weight: 400;
    white-space: nowrap;
  }
  .identity__role {
    margin: 2px 0 0;
    color: var(--taupe);
    font-size: 22px;
  }

  .contacts {
    position: absolute;
    left: 412px;
    top: 262px;
    margin: 0;
    padding: 0;
    list-style: none;
    color: var(--taupe);
    font-size: 20px;
  }
  .contacts li {
    display: flex;
    align-items: center;
    gap: 5px;
    height: 24px;
  }
  .contacts svg { width: 17px; height: 17px; fill: var(--teal); flex: none; }

  .tagline {
    position: absolute;
    left: 0;
    right: 0;
    top: 376px;
    margin: 0;
    text-align: center;
    color: var(--taupe);
    font-size: 24px;
    text-transform: uppercase;
    letter-spacing: -0.3px;
  }
  .tagline em { font-style: normal; color: var(--teal); }
</style>
</head>
<body>
<main class="canvas">
  <section class="card card--front">
    <div class="brand">
      <span class="brand__ring"></span>
      <span class="brand__name">Mabel’s Fitness</span>
    </div>
    <div class="identity">
      <h1 class="identity__name">MABEL QUINT HARLOW</h1>
      <p class="identity__role">Personal Trainer</p>
    </div>
    <ul class="contacts">
      <li>
        <svg viewBox="0 0 24 24" aria-hidden="true"><path d="M6.6 10.8a15.1 15.1 0 0 0 6.6 6.6l2.2-2.2c.3-.3.7-.4 1-.2 1.1.4 2.3.6 3.6.6.6 0 1 .4 1 1V20c0 .6-.4 1-1 1A17 17 0 0 1 3 4c0-.6.4-1 1-1h3.5c.6 0 1 .4 1 1 0 1.3.2 2.5.6 3.6.1.3 0 .7-.2 1z"/></svg>
        <span>0781530462</span>
      </li>
      <li>
        <svg viewBox="0 0 24 24" aria-hidden="true"><path d="M2 5h20v2.2l-10 6-10-6z M2 9.5l10 6 10-6V19H2z"/></svg>
        <span>mabel@mabelsfitstudio.example</span>
      </li>
      <li>
        <svg viewBox="0 0 24 24" aria-hidden="true"><path d="M12 2a10 10 0 1 0 0 20 10 10 0 0 0 0-20zm-1 17.9A8 8 0 0 1 4.2 10l4.8 4.8v1a2 2 0 0 0 2 2zm6.9-2.5a2 2 0 0 0-1.9-1.4h-1v-3a1 1 0 0 0-1-1H8v-2h2a1 1 0 0 0 1-1V7h2a2 2 0 0 0 2-2v-.4a8 8 0 0 1 2.9 12.8z"/></svg>
        <span>www.mabelsfitstudio.example</span>
      </li>
    </ul>
  </section>

  <section class="card card--back">
    <div class="brand">
      <span class="brand__ring"></span>
      <span class="brand__name">Mabel’s Fitness</span>
    </div>
    <p class="tagline">Become your <em>happiest, healthiest</em> and <em>strongest self</em></p>
  </section>
</main>
</body>
</html>
```